Waterproofing Construction company needs letterhead

I need a letterhead design for a commercial waterproofing construction company. We would like to see designs that are contemporary, clean, sleek and use our logo. Our current design is dated. I would also like a cover page (see example) that goes with our letterhead. I would like for the footer to have our address, website, and phone number

Target Market(s)

Customers, potential customers.

Font styles to use
Sans Serif

Requirements
Must have
• logo, website, address, phone numbers, only our colors, tahoma font
• PMS: 295C PMS: 2995C
• CMYK: 100/84/36/39 CMYK: 80/12/1/0
• RGB: 16/44/82 RGB: 0/167/224
• HEX#: #102C52 HEX#: #00A7E0
• Black & White: 100% Black & White: 32%
• Gray Scale: 90% Gray Scale: 32%
Nice to have
• Our "icon" logo attached would be nice somewhere on the page.

```html
<!DOCTYPE html>
<html lang="en">
<head>
<meta charset="utf-8">
<title>Tidewell Letterhead</title>
<link href="https://fonts.googleapis.com/css2?family=Lato:ital,wght@0,400;0,700;0,900;1,400&display=swap" rel="stylesheet">
<style>
  :root {
    --navy: #102C52;
    --sky: #00A7E0;
    --paper: #FFFFFF;
    --ink: #5f6166;
    --ink-dark: #3a3c40;
    --backdrop: #d9cfcc;
  }
  * { box-sizing: border-box; margin: 0; padding: 0; }
  html, body {
    width: 1200px;
    height: 784px;
    overflow: hidden;
    background: var(--backdrop);
    font-family: "Lato", sans-serif;
  }
  .letterhead {
    position: absolute;
    left: 330px;
    top: 10px;
    width: 540px;
    height: 764px;
    background: var(--paper);
    overflow: hidden;
    box-shadow: 0 2px 10px rgba(0,0,0,0.12);
  }
  .brand {
    position: absolute;
    top: 42px;
    right: 46px;
    display: flex;
    align-items: center;
    gap: 8px;
    font-family: "Lato", sans-serif;
    font-weight: 900;
    font-size: 28px;
    letter-spacing: 1px;
    color: var(--navy);
  }
  .brand-square {
    width: 14px;
    height: 14px;
    background: var(--sky);
  }
  .letter-body {
    position: absolute;
    top: 140px;
    left: 62px;
    width: 418px;
    color: var(--ink);
    font-size: 8.6px;
    line-height: 1.55;
  }
  .salutation {
    font-size: 11px;
    color: var(--ink-dark);
    margin-bottom: 18px;
  }
  .letter-body p.paragraph { margin-bottom: 14px; }
  .closing {
    margin-top: 26px;
    color: var(--ink-dark);
  }
  .closing-phrase { font-size: 10.5px; margin-bottom: 6px; }
  .sender-name { font-size: 10.5px; }
  .sender-title { font-size: 7.5px; margin-bottom: 8px; }
  .signature-area {
    width: 90px;
    height: 22px;
    background: linear-gradient(90deg, #e6e7ea, #f2f3f5);
  }
  .footer-wave {
    position: absolute;
    left: 0;
    bottom: 0;
    width: 540px;
    height: 764px;
  }
  .footer-contact {
    position: absolute;
    right: 60px;
    bottom: 28px;
    text-align: right;
    color: var(--paper);
    font-size: 10.5px;
    line-height: 1.45;
  }
  .service-areas { font-size: 11px; }
  .footer-rule {
    display: block;
    width: 22px;
    height: 1px;
    background: var(--paper);
    margin: 7px 0 7px auto;
  }
</style>
</head>
<body>
  <main class="letterhead">
    <svg class="footer-wave" viewBox="0 0 540 764" aria-hidden="true">
      <path d="M0,470 C90,474 160,520 220,590" fill="none" stroke="var(--sky)" stroke-width="4"/>
      <path d="M0,505 C150,505 240,605 360,585 C440,571 500,535 540,520" fill="none" stroke="var(--sky)" stroke-width="10"/>
      <path d="M0,522 C150,522 240,622 360,602 C440,588 500,552 540,537 L540,764 L0,764 Z" fill="var(--navy)"/>
    </svg>

    <header class="brand">
      <span class="brand-name">TIDEWELL</span>
      <span class="brand-square"></span>
    </header>

    <section class="letter-body">
      <p class="salutation">Dear sir/Madam,</p>
      <p class="paragraph">Lorem ipsum dolor sit amet, an vel recteque dissentiet, detracto albucius platonem ex vel, eros repudiandae cu. Atqui aliquando nec an, unum graece adolescens vel ad, id odio scae has, iudico euismod atomorum ius ea, cum ea honestatis quaerendum theophrastus. Mea honestatis quaerendum theophrastus.</p>
      <p class="paragraph">Lorem ipsum dolor sit amet, an vel recteque dissentiet, detracto albucius platonem ex vel, eros repudiandae cu. Atqui aliquando nec an, unum graece adolescens vel ad, id odio scae has, iudico euismod atomorum ius ea, cum ea honestatis quaerendum theophrastus. Mea doming reprimique ex, cu cum obvius assentior posidonium. Quo etiam pertinax ex, te eros repudiandae cu. Atqui aliquando nec an, unum graece adolescens vel ad, id odio scae honestatis quaerendum theophrastus. Mea</p>
      <p class="paragraph">Lorem ipsum dolor sit amet, an vel recteque dissentiet, detracto albucius platonem ex vel, eros repudiandae cu. Atqui aliquando nec an, unum graece adolescens vel ad, id odio scae has, iudico euismod atomorum ius ea, cum ea honestatis quaerendum theophrastus. Mea honestatis quaerendum theophrastus. Mea</p>
      <div class="closing">
        <p class="closing-phrase">Kind Regards</p>
        <p class="sender-name">Daniel Mercer</p>
        <p class="sender-title">Chief Alchemist</p>
        <div class="signature-area" role="img" aria-label="Handwritten signature of the sender"></div>
      </div>
    </section>

    <footer class="footer-contact">
      <p class="service-areas">North Carolina<br>South Carolina<br>Virginia</p>
      <span class="footer-rule"></span>
      <p>P : (800) 555-0142 | M : (555) 204-7719</p>
      <p>W : www.tidewellwp.com</p>
      <p>A : PO Box 450 | Riverton, NC 27000</p>
    </footer>
  </main>
</body>
</html>
```